Business card design needed

I need a business card design for a new online retail business based in Australia. I am unsure of the exact content of what I will be selling but it will be probably women's clothing, accessories, gym wear, gifts and maybe homeware linen. I am wanting a classy design that portrays the image of class/style/upmarket.

Target Market(s)

predominantely women - 20-50 age group

Industry/Entity Type

Retail

Contact Information for Business Card

Purely Radiant
Harriet Quenby
Director
ABN 73214508836
17 Parrish Lane Kelvin Ridge NSW 2291
ph: +61 417 935 284
sales@purelyradiant.com.au

Logo Text

I am open for suggestions here

Requirements
Must have
• The design must be both sides of the card

```html
<!DOCTYPE html>
<html lang="en">
<head>
<meta charset="utf-8">
<title>Purely Radiant – Business Card</title>
<link rel="stylesheet" href="https://fonts.googleapis.com/css2?family=Arimo:wght@700&family=Poiret+One&display=swap">
<style>
  :root {
    --page-bg: #ffffff;
    --label-ink: #000000;
    --brand-pink: #f03ee6;
    --card-black: #000000;
    --card-glow: #3a3a3a;
    --card-white: #ffffff;
    --card-edge: #6e6e6e;
  }
  html, body {
    margin: 0;
    padding: 0;
    overflow: hidden;
    background: var(--page-bg);
  }
  .sheet {
    position: relative;
    width: 1200px;
    height: 885px;
    overflow: hidden;
    background: var(--page-bg);
  }
  .side-label {
    position: absolute;
    top: 0;
    margin: 0;
    font-family: "Arimo", Arial, sans-serif;
    font-weight: 700;
    font-size: 34px;
    line-height: 38px;
    color: var(--label-ink);
    transform: translateX(-50%);
  }
  .side-label--front { left: 203px; }
  .side-label--back { left: 992px; }

  .card {
    position: absolute;
    box-sizing: border-box;
    font-family: "Poiret One", "Josefin Sans", sans-serif;
    color: var(--brand-pink);
    text-align: center;
  }
  .card--front {
    left: 0;
    top: 160px;
    width: 419px;
    height: 725px;
    background: radial-gradient(ellipse 60% 50% at 50% 48%, var(--card-glow) 0%, #1a1a1a 45%, var(--card-black) 100%);
  }
  .card--back {
    left: 784px;
    top: 158px;
    width: 416px;
    height: 727px;
    background: var(--card-white);
    border: 1px solid var(--card-edge);
  }

  .wordmark {
    position: absolute;
    left: 0;
    right: 0;
    display: flex;
    align-items: center;
    justify-content: center;
    gap: 14px;
    margin: 0;
    font-weight: 400;
    color: var(--brand-pink);
  }
  .wordmark__dot {
    width: 16px;
    height: 16px;
    border-radius: 50%;
    background: var(--brand-pink);
  }
  .card--front .wordmark { top: 400px; font-size: 42px; }
  .card--back .wordmark { top: 180px; font-size: 40px; }

  .holder {
    position: absolute;
    top: 356px;
    left: 0;
    right: 0;
  }
  .holder__name {
    margin: 0;
    font-size: 30px;
    line-height: 40px;
  }
  .holder__role {
    margin: 0;
    font-size: 21px;
    line-height: 26px;
  }
  .contact {
    position: absolute;
    top: 478px;
    left: 0;
    right: 0;
    margin: 0;
    font-style: normal;
    font-size: 23px;
    line-height: 30.5px;
  }
  .contact__line { display: block; }
  .contact__line--email { font-size: 21px; }
</style>
</head>
<body>
<main class="sheet">
  <h2 class="side-label side-label--front">Front</h2>
  <h2 class="side-label side-label--back">Back</h2>

  <section class="card card--front" aria-label="Card front">
    <p class="wordmark"><span class="wordmark__name">Purely Radiant</span><span class="wordmark__dot"></span></p>
  </section>

  <section class="card card--back" aria-label="Card back">
    <p class="wordmark"><span class="wordmark__name">Purely Radiant</span></p>
    <div class="holder">
      <p class="holder__name">Harriet Quenby</p>
      <p class="holder__role">Director</p>
    </div>
    <address class="contact">
      <span class="contact__line">ABN 73214508836</span>
      <span class="contact__line">17 Parrish Lane</span>
      <span class="contact__line">Kelvin Ridge NSW 2291</span>
      <span class="contact__line">+61 417 935 284</span>
      <span class="contact__line contact__line--email">sales@purelyradiant.com.au</span>
    </address>
  </section>
</main>
</body>
</html>
```